Web Developer Needs a Business Card Design

I need a personal business card design that represents me as a web developer for potential employers. I would like the background to be a dark color on the front for contrast with my logo and name. The back will have all my information along with a smaller version of the logo. I want something with a modern look and feel, not too conservative. This will be used for potential employers and freelance work.

Industry/Entity Type

Business

Contact Information for Business Card

Front should have my logo and name. The back should have all my personal information which would include: name: Tom Varnuch, phone: 570-614-9083, email: tomvarnuch@mailnest.example, website url: www.tomvarnuch.example, logo, web developer.

Font styles to use
Sans Serif

Requirements
Must have
• Must include my logo. The color palette base color will be the logo color.

```html
<!DOCTYPE html>
<html lang="en">
<head>
<meta charset="utf-8">
<title>Tom Varnuch — Business Card</title>
<link href="https://fonts.googleapis.com/css2?family=Roboto:wght@400&display=swap" rel="stylesheet">
<style>
  :root {
    --backdrop: #a9a6a6;
    --card: #0b0b0b;
    --card-shade: #161616;
    --mint: #5ee3bf;
  }
  * { margin: 0; padding: 0; box-sizing: border-box; }
  html, body { width: 1200px; height: 1200px; overflow: hidden; }
  body {
    background: var(--backdrop);
    font-family: "Roboto", Arial, sans-serif;
    position: relative;
  }
  .card {
    position: absolute;
    left: 244px;
    width: 712px;
    height: 420px;
    border-radius: 22px;
    background: var(--card);
    overflow: hidden;
    color: var(--mint);
  }
  .card--front { top: 118px; }
  .card--back { top: 644px; }
  .card__scene {
    position: absolute;
    inset: 0;
    background:
      radial-gradient(ellipse at 18% 30%, var(--card-shade) 0%, transparent 45%),
      radial-gradient(ellipse at 85% 20%, var(--card-shade) 0%, transparent 40%);
  }
  .brand {
    position: absolute;
    display: flex;
    align-items: center;
    gap: 16px;
    font-size: 34px;
    font-weight: 400;
    color: var(--mint);
    white-space: nowrap;
  }
  .brand__dot {
    width: 22px; height: 22px;
    border-radius: 50%;
    background: var(--mint);
    flex: none;
  }
  .card--front .brand { left: 50%; top: 50%; transform: translate(-50%, -50%); }
  .card--back .brand { left: 400px; top: 186px; font-size: 30px; }
  .identity { position: absolute; left: 37px; top: 38px; }
  .identity__name { font-size: 30px; line-height: 1.2; }
  .identity__role { font-size: 17px; margin-top: 8px; }
  .contacts {
    position: absolute;
    left: 37px; top: 294px;
    list-style: none;
  }
  .contacts li {
    display: flex;
    align-items: center;
    height: 28.5px;
    font-size: 19px;
  }
  .contacts svg { width: 18px; height: 18px; margin-right: 21px; margin-left: 1px; fill: var(--mint); }
</style>
</head>
<body>

<section class="card card--front">
  <div class="card__scene" role="img" aria-label="Faint dark desk scene with a tablet, keyboard and notebook"></div>
  <div class="brand"><span class="brand__dot"></span>Tom Varnuch</div>
</section>

<section class="card card--back">
  <div class="card__scene" role="img" aria-label="Faint dark desk scene with a tablet, keyboard, notebook and coffee cup"></div>
  <div class="identity">
    <h1 class="identity__name" style="font-weight:400">Tom Varnuch</h1>
    <p class="identity__role">Web Developer</p>
  </div>
  <div class="brand"><span class="brand__dot"></span>Tom Varnuch</div>
  <ul class="contacts">
    <li>
      <svg viewBox="0 0 24 24" aria-hidden="true"><path d="M3 8c0-3 4-5 9-5s9 2 9 5v2h-5V8c-1-1-7-1-8 0v2H3z"/><path d="M6 12h12l2 8H4z"/></svg>
      570-614-9083
    </li>
    <li>
      <svg viewBox="0 0 24 24" aria-hidden="true"><path d="M2 5h20v14H2z M4 7l8 6 8-6" fill="var(--mint)"/><path d="M4 7l8 6 8-6" fill="none" stroke="#0b0b0b" stroke-width="2"/></svg>
      tomvarnuch@mailnest.example
    </li>
    <li>
      <svg viewBox="0 0 24 24" aria-hidden="true"><circle cx="12" cy="12" r="9" fill="none" stroke="var(--mint)" stroke-width="2"/><ellipse cx="12" cy="12" rx="4" ry="9" fill="none" stroke="var(--mint)" stroke-width="2"/><path d="M3 12h18" stroke="var(--mint)" stroke-width="2"/></svg>
      www.tomvarnuch.example
    </li>
  </ul>
</section>

</body>
</html>
```